Business card for communications

Need a business card for my consulting business - I work with not for profits, start ups and social enterprises on their media, communications campaigns.

Please see my website for colours, images and fonts www.morvenquillet.example

Morven Quillet
Communications & Campaign strategist
Sydney - Melbourne
M: 0498 317 250
E: morven@morvenquillet.example
S: morvenquillet
W: morvenquillet.example
T: @morvenquillet

(above is info only and can be presented any way e.g. should not have to be M for mobile - it should be an icon)
Updates

Dear designers I have updated the brief and uploaded high res images from my website for you to use. The designs so far with the use of images and icons are much better so far. Thank you I look forward to receiving your revised designs. Morven Quillet

Industry/Entity Type

Communications

Font styles to use
Sans Serif

Requirements
Must have
• Icons for contact details
Images from the website www.morvenquillet.example
Nice to have
• Images - attached

```html
<!DOCTYPE html>
<html lang="en">
<head>
<meta charset="utf-8">
<title>Morven Quillet — Business Cards</title>
<link href="https://fonts.googleapis.com/css2?family=Gelasio:wght@500&family=Jost:wght@400;500&display=swap" rel="stylesheet">
<style>
  :root {
    --backdrop: #332f2a;
    --sun: #ffe500;
    --ink: #111111;
    --paper: #ffffff;
    --wood-light: #b8824a;
    --wood-dark: #7a4e27;
    --portrait-a: #9a8f86;
    --portrait-b: #3a302c;
  }
  * { box-sizing: border-box; margin: 0; padding: 0; }
  html, body { width: 1200px; height: 1200px; overflow: hidden; }
  body {
    background: var(--backdrop);
    position: relative;
    font-family: "Jost", "Futura", sans-serif;
    color: var(--ink);
  }
  .card {
    position: absolute;
    border-radius: 14px;
    overflow: hidden;
    box-shadow: 0 4px 10px rgba(0,0,0,0.45);
  }
  /* Front */
  .card--front { left: 340px; top: 110px; width: 529px; height: 316px; }
  .card__scene {
    position: absolute; inset: 0;
    background:
      radial-gradient(ellipse at 30% 30%, rgba(255,255,255,0.35), transparent 40%),
      radial-gradient(ellipse at 75% 80%, rgba(120,170,200,0.35), transparent 40%),
      linear-gradient(135deg, var(--wood-light), var(--wood-dark));
  }
  .card__band {
    position: absolute; left: 0; right: 0; top: 202px; height: 58px;
    background: var(--sun);
  }
  .card__band-name {
    position: absolute; right: 49px; top: 50%; transform: translateY(-50%);
    font-family: "Gelasio", Georgia, serif;
    font-weight: 500;
    font-size: 29px;
    letter-spacing: 0.3px;
    white-space: nowrap;
  }
  /* Backs */
  .card--back { width: 527px; height: 314px; }
  .card--yellow { left: 340px; top: 466px; background: var(--sun); }
  .card--white { left: 337px; top: 818px; background: var(--paper); }
  .portrait {
    position: absolute; left: 202px; top: 27px; width: 132px; height: 132px;
    border-radius: 50%;
    background: radial-gradient(circle at 50% 40%, var(--portrait-a), var(--portrait-b) 75%);
  }
  .identity {
    position: absolute; right: 274px; top: 181px; text-align: right; white-space: nowrap;
  }
  .identity__name { font-size: 16.5px; font-weight: 400; letter-spacing: 0.2px; line-height: 1.1; }
  .identity__role { font-size: 9.5px; font-weight: 500; line-height: 1.3; }
  .divider {
    position: absolute; left: 266px; top: 188px; bottom: 0; width: 1.3px; background: var(--ink);
  }
  .contacts {
    position: absolute; left: 283px; top: 185px; list-style: none;
  }
  .contacts__item {
    display: flex; align-items: center; height: 20.2px;
    font-size: 13px; white-space: nowrap;
  }
  .contacts__icon { width: 11px; height: 11px; margin-right: 6px; flex: none; }
</style>
</head>
<body>

<section class="card card--front">
  <div class="card__scene" role="img" aria-label="Overhead photo of a shared wooden office desk with computers, keyboards, folders and coffee cups"></div>
  <div class="card__band"><span class="card__band-name">MORVEN QUILLET</span></div>
</section>

<section class="card card--back card--yellow">
  <div class="portrait" role="img" aria-label="Circular portrait photo of Morven Quillet"></div>
  <div class="identity">
    <p class="identity__name">MORVEN QUILLET</p>
    <p class="identity__role">Communications &amp; Campaign Strategist</p>
  </div>
  <div class="divider"></div>
  <ul class="contacts">
    <li class="contacts__item"><svg class="contacts__icon" viewBox="0 0 11 11"><rect x="2.5" y="0.5" width="6" height="10" rx="1.2" fill="none" stroke="#111" stroke-width="1.4"/><rect x="4" y="2" width="3" height="5" fill="#111"/></svg>0498 317 250</li>
    <li class="contacts__item"><svg class="contacts__icon" viewBox="0 0 11 11"><rect x="1" y="2.5" width="9" height="6" fill="#111"/><path d="M1 2.5 L5.5 6 L10 2.5" fill="none" stroke="#ffe500" stroke-width="0.9"/></svg>morven@morvenquillet.example</li>
    <li class="contacts__item"><svg class="contacts__icon" viewBox="0 0 11 11"><circle cx="5.5" cy="5.5" r="4.6" fill="none" stroke="#111" stroke-width="1.3"/><ellipse cx="5.5" cy="5.5" rx="2" ry="4.6" fill="none" stroke="#111" stroke-width="1"/><line x1="1" y1="5.5" x2="10" y2="5.5" stroke="#111" stroke-width="1"/></svg>morvenquillet.example</li>
    <li class="contacts__item"><svg class="contacts__icon" viewBox="0 0 11 11"><circle cx="5.5" cy="5.5" r="5" fill="#111"/></svg>@morvenquillet</li>
    <li class="contacts__item"><svg class="contacts__icon" viewBox="0 0 11 11"><circle cx="5.5" cy="5.5" r="5" fill="#111"/></svg>morvenquillet</li>
  </ul>
</section>

<section class="card card--back card--white">
  <div class="portrait" role="img" aria-label="Circular portrait photo of Morven Quillet"></div>
  <div class="identity">
    <p class="identity__name">MORVEN QUILLET</p>
    <p class="identity__role">Communications &amp; Campaign Strategist</p>
  </div>
  <div class="divider"></div>
  <ul class="contacts">
    <li class="contacts__item"><svg class="contacts__icon" viewBox="0 0 11 11"><rect x="2.5" y="0.5" width="6" height="10" rx="1.2" fill="none" stroke="#111" stroke-width="1.4"/><rect x="4" y="2" width="3" height="5" fill="#111"/></svg>0498 317 250</li>
    <li class="contacts__item"><svg class="contacts__icon" viewBox="0 0 11 11"><rect x="1" y="2.5" width="9" height="6" fill="#111"/><path d="M1 2.5 L5.5 6 L10 2.5" fill="none" stroke="#fff" stroke-width="0.9"/></svg>morven@morvenquillet.example</li>
    <li class="contacts__item"><svg class="contacts__icon" viewBox="0 0 11 11"><circle cx="5.5" cy="5.5" r="4.6" fill="none" stroke="#111" stroke-width="1.3"/><ellipse cx="5.5" cy="5.5" rx="2" ry="4.6" fill="none" stroke="#111" stroke-width="1"/><line x1="1" y1="5.5" x2="10" y2="5.5" stroke="#111" stroke-width="1"/></svg>morvenquillet.example</li>
    <li class="contacts__item"><svg class="contacts__icon" viewBox="0 0 11 11"><circle cx="5.5" cy="5.5" r="5" fill="#111"/></svg>@morvenquillet</li>
    <li class="contacts__item"><svg class="contacts__icon" viewBox="0 0 11 11"><circle cx="5.5" cy="5.5" r="5" fill="#111"/></svg>morvenquillet</li>
  </ul>
</section>

</body>
</html>
```